Hunting business need a new wild boar hunting flyer

We need a flyer design for a company based in Saint-Hénédine, Québec. We are a hunting preserve and this flyer must be made for the Boar hunting market. we don’t have any particular restriction for the format but would prefer a tri-fold. The flyer is intended to be given to customer during trade show. You don’t need to put all the information on the flyer I know I have put a lot of info.

85% of our customer are Male with high school or college scholarship.

I may be wrong, but I would like the flyer to have lot’s of black and with a tough style almost like a biker style. Something not clean and hard but with a professional design.

We don’t do standard, don’t be affraid to submit something special even if it required manual assembling. We need something that will mark the customer in the trade show. Note that the custommer receive at least 30 flyers from competitors as well.

Logo of the company in the files.
See files for photo of wild boar.
Would be nice to add wild boar, wild boar skull are pretty impressive (it’s sanglier in french)

Sample text :

Montrez votre côté rebelle!

Offrez-vous LE trip de chasse entre amis !

Chassez en tout temps et sans permis sur deux magnifiques territoires forestiers de la taille de 30 terrains de football chacun. Les enclos sont situés en Beauce, à 30 minutes de Québec. Le taux de succès est de 100 %. Nous pouvons aussi fournir l'hébergement sur demande. La ferme est ouverte depuis 1982 et a toujours été gérée par des passionnés de la chasse, de la nature et de la bonne venaison.

C’est presque « hors-la-loi »!
• Aucun permis requis
• Succès garanti
• Chasse pendant toute l’année
• Guide sur place et territoire exclusif
• À proximité de Québec

Intense et renversant!

Que vous soyez un chasseur débutant ou vétéran, la chasse au sanglier sera pour vous une expérience extraordinaire. Ce gibier, qui ne vit pas à l’état sauvage au Québec, est un adversaire de taille. Ne vous fiez pas à son allure tranquille. S’il se sent en danger, il n’hésite pas à se sauver à toute vitesse et il n’arrête pas, même si vous vous trouvez sur son chemin. Ce gibier est suffisamment gros pour être chassé avec la plupart des carabines. Il se prête aussi très bien à la chasse au fusil, à l’arc ou à l’arbalète.

C’est bien beau, mais ça goûte quoi?

La chair du sanglier est rouge et elle est plus maigre que celle du porc. Elle est très tendre et succulente. Le sanglier offre les mêmes possibilités de coupe que le porc. Vous pouvez aussi l’essayer en méchoui à l’occasion d’une rencontre de groupe. Vos convives et vous dégusterez alors une venaison exceptionnelle.

Quelques commentaires de nos chasseurs :

« J’ai été surpris de voir à quel point ces animaux peuvent se cacher et se déplacer rapidement. C’est beaucoup plus difficile que je croyais. »
Mathieu, Québec, 2015

« La viande était succulente et tendre. J’ai hâte de revenir récolter un autre sanglier à la ferme. »
Josée, Québec, 2015

Réservez pendant le salon et obtenez le crâne blanchi de votre sanglier gratuitement.

Venez récolter les espèces exotiques suivantes :
Cerf de Virginie (500 $*)
Cerf élaphe (850 $*)
Sika (600 $*)
Daim (500 $*)
Dindon sauvage (85 $*)
Faisan (200 $ pour 10)
Sanglier (350 $*)

*Prix de départ, sujet à changement sans préavis.

Le Domaine des Trois Ruisseaux
148, rang Saint-Ovide
Sainte-Hénédine (Québec) G0R 4K7

Tél. : 418 237-1046
Courriel : info@boisdorval.ranch
Site Web : www.boisdorval.ranch

Target Market(s)

See description

Industry/Entity Type

Hunting

Requirements
Must have
• Hard, rebel or dirty look.

```html
<!DOCTYPE html>
<html lang="fr">
<head>
<meta charset="utf-8">
<title>Le Domaine des Trois Ruisseaux – Dépliant chasse</title>
<link href="https://fonts.googleapis.com/css2?family=Black+Ops+One&family=Lato:wght@400;700&family=Roboto+Condensed:wght@700&family=Arimo:wght@400;700&display=swap" rel="stylesheet">
<style>
:root{
  --page:#8a8a8a;
  --black:#141414;
  --charcoal:#2a2a2a;
  --red:#e3101f;
  --red-dark:#c40d18;
  --white:#ffffff;
  --parchment:#eedcaa;
  --parchment-edge:#d9bf7e;
  --wood:#e2c9a0;
  --wood-dark:#c9a676;
  --ink:#1b1b1b;
  --forest-a:#6b5a3f;
  --forest-b:#3d3426;
}
*{margin:0;padding:0;box-sizing:border-box}
html,body{width:1200px;height:907px;overflow:hidden;background:var(--page)}
.flyer{position:absolute;left:31px;top:47px;width:1138px;height:812px;background:var(--black);overflow:hidden;box-shadow:0 6px 18px rgba(0,0,0,.45)}
.panel{position:absolute;top:0;height:812px;overflow:hidden}
.panel--left{left:0;width:382px;background:linear-gradient(180deg,#3a3024,#1c1914 60%,#2a241c)}
.panel--middle{left:382px;width:372px;background:linear-gradient(180deg,#1a1a1a,#2e2e2e 45%,#151515)}
.panel--right{left:754px;width:384px;background:linear-gradient(180deg,#1e1d1b,#2f2b26 50%,#121212)}
.photo{position:absolute;background:linear-gradient(160deg,var(--forest-a),var(--forest-b))}
.torn{position:absolute;left:0;width:100%}
.intro-box{position:absolute;left:30px;top:191px;width:331px;height:562px;background:linear-gradient(180deg,var(--parchment),var(--parchment-edge));}
.intro-text{position:absolute;left:22px;top:20px;width:288px;font:400 14.6px/1.33 'Lato',sans-serif;color:var(--ink);text-align:justify}
.ribbon{position:absolute;left:0;top:235px;width:307px;height:32px;background:var(--charcoal);clip-path:polygon(0 0,94% 0,100% 50%,94% 100%,0 100%);font:700 16px/32px 'Roboto Condensed',sans-serif;color:var(--red);padding-left:22px;letter-spacing:.3px}
.perks{position:absolute;left:22px;top:290px;list-style:none;font:700 14.5px/1.3 'Lato',sans-serif;color:var(--ink)}
.perks li{padding-left:16px;position:relative}
.perks li::before{content:"";position:absolute;left:2px;top:6px;width:7px;height:7px;border-radius:50%;background:var(--red)}
.intro-photo{left:18px;top:405px;width:295px;height:148px;border:4px solid var(--white)}
.red-top{position:absolute;left:0;top:0;width:372px;height:182px;background:var(--red)}
.tagline{position:absolute;left:0;width:100%;text-align:center}
.tagline--stencil{top:42px;font:400 27px/1 'Black Ops One',sans-serif;color:var(--white)}
.tagline--plain{top:80px;font:400 24px/1 'Arimo',sans-serif;color:var(--ink)}
.species-title{position:absolute;top:225px;left:0;width:100%;text-align:center;font:700 20px/1 'Roboto Condensed',sans-serif;color:var(--red)}
.species-sub{position:absolute;top:254px;left:0;width:100%;text-align:center;font:400 24px/1 'Arimo',sans-serif;color:var(--white)}
.rule{position:absolute;top:301px;left:26px;width:322px;height:3px;background:var(--red)}
.price-box{position:absolute;left:31px;top:338px;width:311px;height:309px;background:linear-gradient(180deg,var(--parchment),var(--parchment-edge));padding:22px 14px 0 12px}
.price{display:flex;align-items:baseline;font:700 15.5px/1 'Lato',sans-serif;color:var(--ink);height:38.4px}
.price .dots{flex:1;border-bottom:2px dotted #444;margin:0 2px;transform:translateY(-3px)}
.price .cost{color:var(--red)}
.contact{position:absolute;top:705px;left:0;width:100%;text-align:center;list-style:none;font:700 16.5px/24px 'Lato',sans-serif;color:var(--white)}
.contact svg{width:15px;height:15px;vertical-align:-2px;margin-right:6px;fill:var(--red)}
.wood-top{position:absolute;left:0;top:0;width:384px;height:182px;background:linear-gradient(100deg,var(--wood),#ecd7b3 50%,var(--wood-dark))}
.brand{position:absolute;left:0;top:70px;width:100%;text-align:center;display:flex;justify-content:center;align-items:center;gap:10px}
.brand-mark{width:14px;height:14px;border-radius:50%;background:var(--red-dark)}
.brand-name{font:700 21px/1.1 'Roboto Condensed',sans-serif;color:var(--red-dark);letter-spacing:.3px}
.hunt-photo{left:44px;top:226px;width:298px;height:334px;border:6px solid var(--white);transform:rotate(-.6deg);background:linear-gradient(170deg,#7a6a4c,#56442e 55%,#3a2e20)}
.slogan{position:absolute;left:0;width:100%;text-align:center}
.slogan--stencil{top:588px;font:400 32px/1 'Black Ops One',sans-serif;color:var(--red)}
.slogan--plain{top:630px;font:400 37px/1 'Arimo',sans-serif;color:var(--white)}
.phone-tag{position:absolute;left:28px;top:712px;width:332px;height:52px;background:linear-gradient(100deg,var(--wood),#ecd7b3);border:3px solid var(--white);text-align:center;font:400 26px/46px 'Arimo',sans-serif;letter-spacing:5px;color:var(--red)}
</style>
</head>
<body>
<main class="flyer">

  <section class="panel panel--left">
    <div class="photo" style="left:0;top:0;width:382px;height:175px" role="img" aria-label="Photo d'un sanglier dans un sous-bois d'automne"></div>
    <svg class="torn" style="top:112px;height:70px" viewBox="0 0 382 70" preserveAspectRatio="none" aria-hidden="true">
      <polygon fill="#e3101f" points="0,40 30,34 60,38 95,28 130,32 170,20 210,24 250,14 290,18 330,8 382,10 382,48 340,42 300,50 260,44 220,54 180,48 140,58 100,52 60,60 20,56 0,60"/>
      <polyline fill="none" stroke="#fff" stroke-width="4" points="0,60 20,56 60,60 100,52 140,58 180,48 220,54 260,44 300,50 340,42 382,48"/>
    </svg>
    <div class="intro-box">
      <p class="intro-text">Chassez en tout temps et sans permis sur deux magnifiques territoires forestiers de la taille de 30 terrains de football chacun. Les enclos sont situés en Beauce, à 30 minutes de Québec. Le taux de succès est de 100 %. Nous pouvons aussi fournir l'hébergement sur demande. La ferme est ouverte depuis 1982 et a toujours été gérée par des passionnés de la chasse, de la nature et de la bonne venaison.</p>
      <div class="ribbon">C'EST PRESQUE « HORS-LA-LOI »</div>
      <ul class="perks">
        <li>Aucun permis requis</li>
        <li>Succès garanti</li>
        <li>Chasse pendant toute l'année</li>
        <li>Guide sur place et territoire exclusif</li>
        <li>À proximité de Québec</li>
      </ul>
      <div class="photo intro-photo" role="img" aria-label="Photo d'un chasseur à l'arc en forêt"></div>
    </div>
  </section>

  <section class="panel panel--middle">
    <div class="red-top"></div>
    <p class="tagline tagline--stencil">OFFREZ-VOUS LE TRIP DE</p>
    <p class="tagline tagline--plain">CHASSE ENTRE AMIS !</p>
    <svg class="torn" style="top:140px;height:60px" viewBox="0 0 372 60" preserveAspectRatio="none" aria-hidden="true">
      <polygon fill="#1a1a1a" points="0,32 40,26 80,34 120,22 160,30 200,18 240,28 280,20 320,30 372,24 372,60 0,60"/>
      <polyline fill="none" stroke="#fff" stroke-width="4" points="0,32 40,26 80,34 120,22 160,30 200,18 240,28 280,20 320,30 372,24"/>
    </svg>
    <h2 class="species-title">VENEZ RÉCOLTER LES ESPÈCES</h2>
    <p class="species-sub">EXOTIQUES SUIVANTES</p>
    <div class="rule"></div>
    <div class="price-box">
      <div class="price"><span>Cerf de Virginie</span><span class="dots"></span><span class="cost">(500 $*)</span></div>
      <div class="price"><span>Cerf élaphe</span><span class="dots"></span><span class="cost">(850 $*)</span></div>
      <div class="price"><span>Sika</span><span class="dots"></span><span class="cost">(600 $*)</span></div>
      <div class="price"><span>Daim</span><span class="dots"></span><span class="cost">(500 $*)</span></div>
      <div class="price"><span>Dindon sauvage</span><span class="dots"></span><span class="cost">(85 $*)</span></div>
      <div class="price"><span>Faisan</span><span class="dots"></span><span class="cost">(200 $ pour 10)</span></div>
      <div class="price"><span>Sanglier</span><span class="dots"></span><span class="cost">(350 $*)</span></div>
    </div>
    <ul class="contact">
      <li><svg viewBox="0 0 16 16"><path d="M3 1l3 3-2 2c1 2 3 4 5 5l2-2 3 3-2 3C7 15 1 9 1 3z"/></svg>418 237-1046</li>
      <li><svg viewBox="0 0 16 16"><path d="M1 3h14v10H1z M1 3l7 6 7-6" stroke="#1a1a1a" stroke-width="1"/></svg>info@boisdorval.ranch</li>
      <li><svg viewBox="0 0 16 16"><circle cx="8" cy="8" r="6"/></svg>www.boisdorval.ranch</li>
    </ul>
  </section>

  <section class="panel panel--right">
    <div class="wood-top"></div>
    <div class="brand">
      <span class="brand-mark"></span>
      <span class="brand-name">LE DOMAINE DES TROIS RUISSEAUX</span>
    </div>
    <svg class="torn" style="top:158px;height:40px" viewBox="0 0 384 40" preserveAspectRatio="none" aria-hidden="true">
      <polygon fill="#1e1d1b" points="0,20 40,14 80,22 120,12 160,20 200,10 240,18 280,12 320,20 384,14 384,40 0,40"/>
      <polyline fill="none" stroke="#fff" stroke-width="4" points="0,20 40,14 80,22 120,12 160,20 200,10 240,18 280,12 320,20 384,14"/>
    </svg>
    <div class="photo hunt-photo" role="img" aria-label="Photo d'un chasseur visant un sanglier dans la forêt"></div>
    <h1 class="slogan slogan--stencil">MONTREZ VOTRE</h1>
    <p class="slogan slogan--plain">CÔTÉ REBELLE!</p>
    <div class="phone-tag">418-237-1046</div>
  </section>

</main>
</body>
</html>
```